Vesk Architecture

We are a architectural design and build company working between scales 1/1000 to 1/1 we want people to understand our difference from our design experience and quality.we build hotels restourants and office spaces.Our company name is Vesk architecture to mind sustainability.

We want to write our adress phone and work spesifications on the card and we want our logo as backround.

Ps:you could find the logo adress and phone box numbers from the web:www.veskmimarlik-ornek.com

Target Market(s)

Who looks for experts.

Industry/Entity Type

Architecture

Requirements
Must have
• Design is over everything.
Should not have
• we don want it to be colorfull

```html
<!DOCTYPE html>
<html lang="tr">
<head>
<meta charset="utf-8">
<title>Vesk Architecture – Business Card</title>
<link rel="stylesheet" href="https://fonts.googleapis.com/css2?family=Barlow:wght@300;400;600&display=swap">
<style>
  :root {
    --backdrop: #ececec;
    --card: #050505;
    --ink: #ffffff;
    --ink-soft: #cfcfcf;
    --mark-faint: #2e2e2e;
  }
  html, body {
    margin: 0;
    padding: 0;
    width: 1200px;
    height: 920px;
    overflow: hidden;
    background: var(--backdrop);
  }
  .stage {
    position: relative;
    width: 1200px;
    height: 920px;
    font-family: "Barlow", Arial, sans-serif;
  }
  .card {
    position: absolute;
    background: var(--card);
    color: var(--ink);
  }
  .card--front {
    left: 124px;
    top: 136px;
    width: 402px;
    height: 406px;
  }
  .card--back {
    left: 506px;
    top: 406px;
    width: 418px;
    height: 380px;
  }
  .wordmark {
    position: absolute;
    left: 52px;
    top: 100px;
    font-weight: 300;
    color: var(--ink);
  }
  .wordmark__name {
    display: block;
    font-size: 128px;
    line-height: 1;
    letter-spacing: 2px;
  }
  .wordmark__sub {
    display: block;
    margin-top: 14px;
    font-size: 30px;
    letter-spacing: 4px;
  }
  .contact {
    position: absolute;
    left: 58px;
    top: 112px;
    font-size: 15px;
    line-height: 20px;
    color: var(--ink-soft);
  }
  .contact__name {
    margin: 0;
    font-weight: 600;
    color: var(--ink);
  }
  .contact__role {
    margin: 0;
  }
  .contact__mark {
    margin: 10px 0 12px;
    font-size: 54px;
    line-height: 56px;
    font-weight: 300;
    color: var(--mark-faint);
  }
  .contact__address,
  .contact__lines {
    margin: 0;
  }
  .contact__lines {
    margin-top: 0;
    padding: 0;
    list-style: none;
  }
  .contact__label {
    font-weight: 600;
    color: var(--ink);
  }
</style>
</head>
<body>
  <main class="stage">
    <section class="card card--front" aria-label="Card front">
      <div class="wordmark">
        <span class="wordmark__name">vesk</span>
        <span class="wordmark__sub">MİMARLIK</span>
      </div>
    </section>

    <section class="card card--back" aria-label="Card back">
      <div class="contact">
        <p class="contact__name">Deniz Arman KORAY</p>
        <p class="contact__role">Mimar</p>
        <div class="contact__mark" aria-hidden="true">vesk</div>
        <p class="contact__address">Yelkenli Mah. Liman Cad. Defne Sok.<br>No: 7 Kadıköy / ISTANBUL</p>
        <ul class="contact__lines">
          <li><span class="contact__label">t.</span> 0216 555 01 24</li>
          <li><span class="contact__label">f.</span> 0216 555 01 25</li>
          <li><span class="contact__label">e.</span>info@veskmimarlik-ornek.com</li>
        </ul>
      </div>
    </section>
  </main>
</body>
</html>
```